Two (Similar) Posters - Both 11" x 17"

We are looking for two posters - both 11" x 17" (vertical orientation) - to promote two consecutive, cardiology-related events:

Poster #1) The Inaugural New York ROC Brainbuzz Competition, Cocktail Reception and Whiskey Tasting (http://hb-pvl.org/brainbuzz-and-reception)

and

Poster #2) The 89th Annual Scientific Session and 27th Annual Meeting (http://hb-pvl.org/2017annualmtg)

#1 is a cocktail party with a whiskey tasting that will also feature a gameshow-like event with the med students, and #2 is an educational conference for doctors

Target Market(s)

Healthcare providers (Please do not include stock images of medical professionals; in fact, please use caution with any stock imagery, as it most likely will not be appropriate.)

Industry/Entity Type

Education

Colors

Designer to choose colors to be used in the design.

Requirements
Must have
• Each poster design should include:
• - the 4 logos of the participating organizations (I can upload various other versions if needed) along with the "wording" that goes alongside each one (see "STD_small" image as an example)
• - name of event
• - date, time and location
• - where to register
• - where to get more information
• - some artistic flavor or detailing
• Final (raw) files in an .ai, .psd, .eps or .idml format are required upon project completion.
Nice to have
• It's not crucial that these two posters "match," but it would be nice if they at least coordinated with each other. Would be nice if the designer could stay close to our color scheme (can be found here - http://hb-pvl.org/), but this isn't crucial. Posters should be upscale, neat and professional.
Should not have
• Should not be too difficult to read. These are posters that will likely be hanging on a bulletin board in hospital staff break rooms. Should not be too cartoon-like or silly. The two should not look EXACTLY the same in case people think that they are the same poster.

```html
<!DOCTYPE html>
<html lang="en">
<head>
<meta charset="utf-8">
<title>The 89th Annual Scientific Session &amp; 27th Annual Meeting</title>
<link rel="stylesheet" href="https://fonts.googleapis.com/css2?family=Cormorant+Garamond:wght@500;600&family=Crimson+Text:wght@400&display=swap">
<style>
  :root {
    --navy: #0c1a6e;
    --gold: #c8a84e;
    --gold-pale: #f3e6bd;
    --paper: #ffffff;
    --mist: #e8eef0;
    --ink: #111111;
    --link: #6fb3e8;
  }
  * { margin: 0; padding: 0; box-sizing: border-box; }
  html, body { width: 777px; height: 1200px; overflow: hidden; background: var(--navy); }
  .poster { position: relative; width: 777px; height: 1200px; background: var(--navy); }
  .frame { position: absolute; left: 56px; top: 56px; width: 666px; height: 1088px; background: var(--gold); }
  .sheet { position: absolute; left: 69px; top: 69px; width: 640px; height: 1061px; background: var(--paper); overflow: hidden; }
  .sunburst-art {
    position: absolute; left: 0; top: 0; width: 640px; height: 330px;
    background: radial-gradient(ellipse 360px 300px at 50% 0%, var(--gold-pale) 0%, rgba(243,230,189,0.55) 45%, rgba(255,255,255,0) 100%);
  }
  .display { font-family: "Cormorant Garamond", Georgia, serif; font-weight: 500; color: var(--navy); text-align: center; position: absolute; left: 0; width: 640px; }
  .title-line { font-size: 41px; line-height: 1; }
  .title-1 { top: 224px; }
  .title-amp { top: 281px; }
  .title-2 { top: 336px; }
  .rule { position: absolute; left: 42px; width: 556px; height: 2px; background: var(--gold); }
  .rule-top { top: 416px; }
  .rule-bottom { top: 664px; }
  .date { top: 445px; font-size: 37px; line-height: 1; }
  .time { top: 487px; font-size: 37px; line-height: 1; }
  .venue { top: 533px; font-size: 21px; line-height: 27px; }
  .register { top: 613px; font-size: 21px; }
  .register a { color: var(--link); }
  .summary {
    position: absolute; left: 40px; width: 560px; top: 686px;
    font-family: "Crimson Text", Georgia, serif; font-size: 14px; line-height: 20px;
    color: var(--ink); text-align: center;
  }
  .partners-band { position: absolute; left: 0; top: 825px; width: 640px; height: 236px; background: var(--mist); }
  .partners { position: absolute; top: 34px; left: 0; width: 640px; display: flex; justify-content: center; gap: 26px; }
  .partner { width: 108px; display: flex; flex-direction: column; align-items: center; }
  .partner-mark { width: 62px; height: 62px; border-radius: 50%; background: var(--navy); }
  .partner-name {
    margin-top: 8px; font-family: "Crimson Text", Georgia, serif; font-size: 13px; line-height: 15px;
    color: var(--navy); text-align: center;
  }
  .contact {
    position: absolute; left: 0; width: 640px; top: 168px;
    font-family: "Crimson Text", Georgia, serif; font-size: 15px; line-height: 22px;
    color: var(--ink); text-align: center;
  }
</style>
</head>
<body>
<div class="poster">
  <div class="frame"></div>
  <div class="sheet">
    <div class="sunburst-art" role="img" aria-label="Gold sunburst rays behind a line-drawn handshake flanked by scroll flourishes"></div>

    <h1 class="display title-line title-1">The 89th Annual Scientific Session</h1>
    <div class="display title-line title-amp">&amp;</div>
    <div class="display title-line title-2">27th Annual Meeting</div>

    <div class="rule rule-top"></div>
    <div class="display date">Thursday, Dec. 7th, 2017</div>
    <div class="display time">7:30 A.M. - 3:00 P.M.</div>
    <div class="display venue">Location:<br>The Prince Regent Ballroom<br>42 E. 31st St., New York, NY</div>
    <div class="display register">Register online at <a href="http://hb-pvl.org/2017annualmtg">hb-pvl.org/2017annualmtg</a></div>
    <div class="rule rule-bottom"></div>

    <p class="summary">The Annual Scientific Session brings together cardiologists, cardia-thoracic surgeons, internists, family practitioners, gerontologists, oncologists, cardiac nurse practitioners, physician assistants, cardiology fellows in training (ROCs) and all members of the cardiac care team, and, this year, will feature the winners of the Annual Young Investigators' Competition for case studies and abstracts (posters), which is now open!</p>

    <div class="partners-band">
      <div class="partners">
        <div class="partner"><div class="partner-mark"></div><div class="partner-name">Harbor Heart Center</div></div>
        <div class="partner"><div class="partner-mark"></div><div class="partner-name">Collegium of Cardiac Care</div></div>
        <div class="partner"><div class="partner-mark"></div><div class="partner-name">Hudson–Plata Exchange</div></div>
        <div class="partner"><div class="partner-mark"></div><div class="partner-name">Metro Cardiology Guild</div></div>
      </div>
      <p class="contact">For more information or to inquire about becoming an<br>exhibitor, call (212) 555-0148 or email ask@hb-pvl.org</p>
    </div>
  </div>
</div>
</body>
</html>
```